Fashion clothing business needs a label, swing tag and business card.

Independent womenswear label called "Tessa Wrenly".
I'd like a design for a woven label to go on the clothes, a swing tag and business card design. The design should be simple, modern but timeless. Its a small business, made locally in Melbourne, Australia, produces quality garments for everyday wear using beautiful fabrics.

Reason: just waiting for a few others to submit their designs.

Target Market(s)

30+ ladies, who want quality everyday wear, who don't necessarily follow trends. They can be a bit edgy and willing to take a risk with something different.

Industry/Entity Type

Clothing

Font styles to use
Other font styles liked:
• I dont mind the typewriter font, but can it look modern? happy for you to choose.

Requirements
Should not have
• A difficult shape swing tag - as it might be more expensive for me to get printed and cut.

```html
<!DOCTYPE html>
<html lang="en">
<head>
<meta charset="utf-8">
<title>Tessa Wrenly – Label, Swing Tag &amp; Business Card</title>
<link rel="stylesheet" href="https://fonts.googleapis.com/css2?family=Josefin+Slab:wght@300;400&display=swap">
<style>
  :root {
    --ink: #2b2b2b;
    --paper: #ffffff;
    --line: #000000;
    --ghost-ring: #3b3b3b;
    --field: #737373;
    --stripe-tone: #ececec;
    --text-light: #ffffff;
    --text-dark: #3a3a3a;
  }
  * { box-sizing: border-box; margin: 0; padding: 0; }
  html, body { width: 1200px; height: 1000px; overflow: hidden; background: var(--paper); }
  body { font-family: "Josefin Slab", "Courier New", serif; font-weight: 300; color: var(--text-light); }

  .canvas { position: relative; width: 1200px; height: 1000px; background: var(--paper); }
  .sheet-frame { position: absolute; left: 24px; top: 18px; width: 1153px; height: 963px; border: 3px solid var(--line); }

  .abs { position: absolute; }
  .centered { position: absolute; left: 0; right: 0; text-align: center; white-space: nowrap; }

  /* brand banner */
  .brand-banner { position: absolute; left: 50px; top: 18px; width: 296px; height: 188px; }
  .brand-banner svg { position: absolute; inset: 0; }
  .brand-banner .brand-name { top: 102px; font-size: 48px; font-weight: 300; }

  .ring { position: absolute; border-radius: 50%; }

  /* woven labels */
  .woven-label { position: absolute; background: var(--ink); overflow: hidden; }
  .woven-label--size { left: 113px; top: 316px; width: 433px; height: 259px; }
  .woven-label--plain { left: 588px; top: 316px; width: 517px; height: 259px; }
  .inner-frame { position: absolute; inset: 9px; border: 2px solid var(--text-light); }

  .woven-label--size .ring { left: 155px; top: 27px; width: 124px; height: 124px; border: 2px solid var(--ghost-ring); }
  .woven-label--size .brand-name { top: 58px; font-size: 56px; }
  .woven-label--size .origin { top: 138px; font-size: 21px; letter-spacing: 0.5px; }
  .woven-label--size .size-mark { top: 205px; font-size: 23px; letter-spacing: 1px; }

  .woven-label--plain .ring { left: 200px; top: 66px; width: 118px; height: 118px; border: 2px solid var(--ghost-ring); }
  .woven-label--plain .brand-name { top: 97px; font-size: 46px; }
  .woven-label--plain .origin { top: 160px; font-size: 14px; letter-spacing: 0.4px; }

  /* business card */
  .business-card { position: absolute; left: 102px; top: 593px; width: 455px; height: 259px; background: var(--ink); }
  .business-card .texture { position: absolute; left: 36px; top: 0; width: 214px; height: 259px; background: var(--stripe-tone); }
  .business-card .card-name { position: absolute; left: 36px; width: 214px; top: 95px; text-align: center; font-size: 26px; color: var(--text-dark); }
  .contact-line { position: absolute; left: 47px; display: flex; align-items: center; gap: 5px; font-size: 14px; color: var(--text-dark); font-weight: 400; }
  .contact-line svg { width: 13px; height: 13px; fill: var(--ink); }
  .contact-line--mail { top: 130px; }
  .contact-line--phone { top: 156px; }
  .business-card .seal { left: 312px; top: 86px; width: 86px; height: 86px; background: var(--paper); }

  /* swing tag back */
  .swing-tag { position: absolute; left: 588px; top: 593px; width: 517px; height: 259px; background: var(--ink); }
  .tag-field { position: absolute; left: 0; height: 26px; display: flex; align-items: center; }
  .tag-field .field-label { position: absolute; right: 365px; width: 120px; text-align: right; font-size: 20px; }
  .tag-field .field-bar { position: absolute; left: 167px; width: 264px; height: 26px; background: var(--field); }
  .tag-field--size { top: 53px; width: 517px; }
  .tag-field--style { top: 106px; width: 517px; }
  .tag-field--price { top: 159px; width: 517px; }
  .swing-tag .tag-contact { top: 210px; font-size: 15px; letter-spacing: 0.3px; }
</style>
</head>
<body>
<main class="canvas">
  <div class="sheet-frame"></div>

  <section class="brand-banner">
    <svg width="296" height="188" viewBox="0 0 296 188" aria-hidden="true">
      <path d="M0 0 H296 V180 Q150 176 0 187 Z" fill="var(--ink)"/>
      <circle cx="147" cy="62" r="34" fill="none" stroke="var(--text-light)" stroke-width="2"/>
    </svg>
    <div class="centered brand-name">Tessa Wrenly</div>
  </section>

  <section class="woven-label woven-label--size">
    <div class="ring"></div>
    <div class="centered brand-name">Tessa Wrenly</div>
    <div class="centered origin">MADE IN AUSTRALIA</div>
    <div class="centered size-mark">SIZE: M</div>
  </section>

  <section class="woven-label woven-label--plain">
    <div class="inner-frame"></div>
    <div class="ring"></div>
    <div class="centered brand-name">Tessa Wrenly</div>
    <div class="centered origin">MADE IN AUSTRALIA</div>
  </section>

  <section class="business-card">
    <div class="texture" role="img" aria-label="Light grey diagonal pinstripe texture panel"></div>
    <div class="card-name">Tessa Wrenly</div>
    <div class="contact-line contact-line--mail">
      <svg viewBox="0 0 16 16" aria-hidden="true"><path d="M1 3h14v10H1z"/><path d="M1 3l7 6 7-6" fill="none" stroke="var(--stripe-tone)" stroke-width="1.4"/></svg>
      <span>INFO@TESSAWRENLY.COM</span>
    </div>
    <div class="contact-line contact-line--phone">
      <svg viewBox="0 0 16 16" aria-hidden="true"><rect x="3" y="0" width="10" height="16" rx="1"/><rect x="5" y="2" width="6" height="8" fill="var(--stripe-tone)"/></svg>
      <span>0400 318 562</span>
    </div>
    <div class="ring seal"></div>
  </section>

  <section class="swing-tag">
    <div class="inner-frame"></div>
    <div class="tag-field tag-field--size"><span class="field-label">SIZE</span><span class="field-bar"></span></div>
    <div class="tag-field tag-field--style"><span class="field-label">STYLE</span><span class="field-bar"></span></div>
    <div class="tag-field tag-field--price"><span class="field-label">PRICE</span><span class="field-bar"></span></div>
    <div class="centered tag-contact">INFO@TESSAWRENLY.COM</div>
  </section>
</main>
</body>
</html>
```